Business Card and Letterhead Design Project

I am starting my own building design business in Melbourne. The business will use my experience to help people make balanced life choices for building and renovating. My target audience is women -particularly mothers. I aim to be approachable and economical. I would like to see a design that uses greens or blues - natural colours. A lot of my work balances design and construction management so design should be flexible.

I want a double sided business card design and a letterhead design that I can use on all office correspondance

Design should have a clean crisp feel - a bit edgey in a feminine way.

Target Market(s)

Potential clients.

Industry/Entity Type

Construction

Requirements
Must have
• Harbourline Design Studio
Rosalind Tebbutt B.Arch

0498 273 461
rosalind@harbourlinedesignstudio.com.au

14 Quandong Street
Ashbury Vale VIC 3187
harbourlinedesignstudio.com.au
Nice to have
• Should have a calming feel to make me seem approachable but still professional.
Should not have
• No photos on the card or building plans.

```html
<!DOCTYPE html>
<html lang="en">
<head>
<meta charset="utf-8">
<title>Harbourline Design Studio – Business Card</title>
<link rel="stylesheet" href="https://fonts.googleapis.com/css2?family=Questrial&display=swap">
<style>
  :root {
    --leaf: #8cc63f;
    --leaf-deep: #7ab62e;
    --paper: #ffffff;
    --ink-blue: #1a6fb5;
    --backdrop: #e4e6e3;
    --shadow: rgba(0, 0, 0, 0.18);
  }
  * { box-sizing: border-box; margin: 0; padding: 0; }
  html, body { width: 1200px; height: 900px; overflow: hidden; }
  body {
    background: var(--backdrop);
    font-family: "Questrial", "Century Gothic", sans-serif;
    position: relative;
  }
  .card {
    position: absolute;
    width: 520px;
    height: 300px;
    border-radius: 20px;
    overflow: hidden;
    box-shadow: 0 12px 30px var(--shadow);
  }

  /* Front */
  .card-front {
    left: 150px;
    top: 120px;
    background: var(--leaf);
    color: var(--paper);
  }
  .front-brand {
    position: absolute;
    left: 50px;
    right: 30px;
    top: 82px;
    display: flex;
    align-items: center;
    gap: 14px;
  }
  .brand-square {
    flex: none;
    width: 22px;
    height: 22px;
    background: var(--paper);
  }
  .front-name {
    font-size: 34px;
    line-height: 1.1;
    white-space: nowrap;
    color: var(--paper);
  }
  .front-web {
    position: absolute;
    left: 0;
    right: 30px;
    bottom: 22px;
    text-align: right;
    font-size: 15px;
    letter-spacing: 3px;
    color: var(--ink-blue);
  }

  /* Back */
  .card-back {
    left: 530px;
    top: 480px;
    background: var(--paper);
  }
  .back-brand {
    position: absolute;
    left: 28px;
    top: 34px;
    display: flex;
    align-items: center;
    gap: 10px;
  }
  .back-brand .brand-square { background: var(--leaf); width: 16px; height: 16px; }
  .back-name {
    font-size: 26px;
    white-space: nowrap;
    color: var(--leaf-deep);
  }
  .grid-panel {
    position: absolute;
    left: 0;
    top: 128px;
    width: 230px;
    height: 172px;
    background: linear-gradient(90deg, rgba(140,198,63,0) 0%, rgba(140,198,63,0.55) 55%, var(--leaf) 100%);
  }
  .contact-panel {
    position: absolute;
    left: 230px;
    top: 128px;
    right: 0;
    bottom: 0;
    background: var(--leaf);
    color: var(--paper);
    padding: 12px 18px 14px 10px;
  }
  .person {
    font-size: 18px;
    color: var(--ink-blue);
    margin-bottom: 8px;
  }
  .contact-line {
    font-size: 13px;
    line-height: 1.55;
    white-space: nowrap;
  }
  .address {
    position: absolute;
    right: 18px;
    bottom: 12px;
    text-align: right;
    font-size: 13px;
    line-height: 1.5;
  }
</style>
</head>
<body>
  <section class="card card-front">
    <div class="front-brand">
      <span class="brand-square"></span>
      <span class="front-name">Harbourline Design Studio</span>
    </div>
    <p class="front-web">www.harbourlinedesignstudio.com.au</p>
  </section>

  <section class="card card-back">
    <div class="back-brand">
      <span class="brand-square"></span>
      <span class="back-name">Harbourline Design Studio</span>
    </div>
    <div class="grid-panel" role="img" aria-label="Decorative fading grid of green squares"></div>
    <div class="contact-panel">
      <p class="person">Rosalind Tebbutt B.Arch</p>
      <p class="contact-line">0498 273 461</p>
      <p class="contact-line">rosalind@harbourlinedesignstudio.com.au</p>
      <p class="contact-line">harbourlinedesignstudio.com.au</p>
      <p class="address">14 Quandong Street<br>Ashbury Vale VIC 3187</p>
    </div>
  </section>
</body>
</html>
```